1 Page Software Marketing/Sales Flyer Slick

Bramble Dynamics manufactures several software packages that we sell. We need a 1 page sales/marketing flyer slick that we will allow people to download from our site or as physical leave behinds in meetings. This 1 page slick should be visually (graphically) pleasing while carrying our message for selling our software product.

Target Market(s)

Enterprise Business Customers

Industry/Entity Type

Voip

Requirements
Must have
• Graphical representation of some hot point features, 1 Page - See PDF Detailed Description
Nice to have
• See PDF Detailed Description

```html
<!DOCTYPE html>
<html lang="en">
<head>
<meta charset="utf-8">
<title>Bramble Dynamics – BDX CDR Software Screen Shots</title>
<link href="https://fonts.googleapis.com/css2?family=Lato:wght@300;400&family=Ubuntu:wght@500&display=swap" rel="stylesheet">
<style>
  :root{
    --teal:#6cc3d3;
    --navy:#1f3f6e;
    --yellow:#f4e61c;
    --white:#ffffff;
    --green:#7db86d;
    --red:#a3202e;
    --gold:#d1b82c;
    --grey:#c4c4c4;
    --ink:#333333;
  }
  html,body{margin:0;padding:0;overflow:hidden;}
  body{width:927px;height:1200px;position:relative;background:var(--white);font-family:'Lato',sans-serif;}
  .band{position:absolute;left:0;width:927px;background:var(--teal);}
  .band-header{top:0;height:156px;}
  .band-divider-one{top:434px;height:55px;}
  .band-divider-two{top:768px;height:54px;}
  .band-footer{top:1102px;height:98px;}
  .brand{position:absolute;left:56px;top:28px;display:flex;align-items:center;gap:18px;}
  .brand-dot{width:92px;height:92px;border-radius:50%;background:var(--navy);}
  .brand-name{font-family:'Lato',sans-serif;font-weight:300;font-size:38px;color:var(--navy);}
  .flyer-title{position:absolute;right:55px;top:60px;margin:0;font-family:'Ubuntu',sans-serif;font-weight:500;font-size:21px;color:var(--yellow);}
  .page-number{position:absolute;right:42px;top:1143px;font-family:'Ubuntu',sans-serif;font-weight:500;font-size:19px;color:var(--white);}
  .charts{position:absolute;left:0;top:0;}
  .lbl{font-family:'Lato',sans-serif;font-size:7px;fill:var(--ink);}
  .axis{font-family:'Lato',sans-serif;font-size:6.5px;fill:#555;}
  .tab{font-family:'Lato',sans-serif;font-size:3.5px;fill:#3a7bd5;}
  .tab-dim{font-family:'Lato',sans-serif;font-size:3.5px;fill:#666;}
</style>
</head>
<body>
  <div class="band band-header"></div>
  <div class="band band-divider-one"></div>
  <div class="band band-divider-two"></div>
  <div class="band band-footer"></div>

  <div class="brand"><div class="brand-dot"></div><span class="brand-name">Bramble Dynamics</span></div>
  <h1 class="flyer-title">BDX CDR Software Screen Shots</h1>
  <div class="page-number">2/2</div>

  <svg class="charts" width="927" height="1200" viewBox="0 0 927 1200">
    <defs>
      <g id="pie">
        <path d="M0,0 L0,-66 A66,66 0 1 1 -62,-22.6 Z" fill="#7db86d"/>
        <path d="M0,0 L-62,-22.6 A66,66 0 0 1 -27.9,-59.8 Z" fill="#a3202e"/>
        <path d="M0,0 L-27.9,-59.8 A66,66 0 0 1 0,-66 Z" fill="#d1b82c"/>
      </g>
      <g id="lines">
        <g stroke="#e4e4e4" stroke-width="1">
          <line x1="0" y1="0" x2="274" y2="0"/><line x1="0" y1="19.75" x2="274" y2="19.75"/>
          <line x1="0" y1="39.5" x2="274" y2="39.5"/><line x1="0" y1="59.25" x2="274" y2="59.25"/>
          <line x1="0" y1="79" x2="274" y2="79"/><line x1="0" y1="98.75" x2="274" y2="98.75"/>
          <line x1="0" y1="118.5" x2="274" y2="118.5"/><line x1="0" y1="138.25" x2="274" y2="138.25"/>
          <line x1="11" y1="0" x2="11" y2="158"/><line x1="62" y1="0" x2="62" y2="158"/>
          <line x1="114" y1="0" x2="114" y2="158"/><line x1="167" y1="0" x2="167" y2="158"/>
          <line x1="220" y1="0" x2="220" y2="158"/><line x1="272" y1="0" x2="272" y2="158"/>
        </g>
        <line x1="0" y1="158" x2="274" y2="158" stroke="#999" stroke-width="1"/>
        <line x1="0" y1="0" x2="0" y2="158" stroke="#999" stroke-width="1"/>
        <g fill="none" stroke-width="1.2">
          <polyline points="11,0 62,126.4 114,140.2 167,126.4 220,124.4 272,134.3" stroke="#bdbdbd"/>
          <polyline points="11,63.2 62,140.2 114,146.2 167,136.3 220,140.2 272,140.2" stroke="#7db86d"/>
          <polyline points="11,150.1 62,148.1 114,152.1 167,149.3 220,146.9 272,154.1" stroke="#d1b82c"/>
          <polyline points="11,144.2 62,153.3 114,154.8 167,154.8 220,153.3 272,156" stroke="#a3202e"/>
        </g>
      </g>
      <g id="legend">
        <rect x="0" y="0" width="60" height="60" fill="#f2f2f2"/>
        <rect x="6" y="14" width="7" height="7" fill="#7db86d"/>
        <rect x="6" y="26" width="7" height="7" fill="#a3202e"/>
        <rect x="6" y="38" width="7" height="7" fill="#d1b82c"/>
        <rect x="6" y="50" width="7" height="7" fill="#bdbdbd"/>
      </g>
      <pattern id="rows" width="52" height="9" patternUnits="userSpaceOnUse">
        <rect width="52" height="9" fill="#ffffff"/>
        <rect x="3" y="3.5" width="18" height="1.6" fill="#b5b5b5"/>
        <line x1="0" y1="8.6" x2="52" y2="8.6" stroke="#e3e3e3" stroke-width="0.6"/>
      </pattern>
      <pattern id="rows-tight" width="44" height="7" patternUnits="userSpaceOnUse">
        <rect width="44" height="7" fill="#ffffff"/>
        <rect x="3" y="2.6" width="14" height="1.3" fill="#b5b5b5"/>
        <line x1="0" y1="6.7" x2="44" y2="6.7" stroke="#e3e3e3" stroke-width="0.5"/>
      </pattern>
    </defs>

    <!-- Feature: call status pie -->
    <use href="#pie" transform="translate(250,296)"/>
    <polyline points="222,200 114,200" fill="none" stroke="#d1b82c" stroke-width="0.8"/>
    <line x1="222" y1="200" x2="233" y2="238" stroke="#d1b82c" stroke-width="0.8"/>
    <text class="lbl" x="114" y="202">REDIRECTED</text>
    <polyline points="106,230 178,230 210,254" fill="none" stroke="#a3202e" stroke-width="0.8"/>
    <text class="lbl" x="106" y="232">NOT ANSWER...</text>
    <polyline points="296,350 312,378 348,378" fill="none" stroke="#7db86d" stroke-width="0.8"/>
    <text class="lbl" x="348" y="380">ANSWERED</text>
    <rect x="225" y="197" width="48" height="27" rx="2" fill="#333"/>
    <path d="M245,224 L249,229 L253,224 Z" fill="#333"/>
    <text x="249" y="208" text-anchor="middle" font-family="Lato,sans-serif" font-size="7" fill="#fff">Answered</text>
    <text x="249" y="219" text-anchor="middle" font-family="Lato,sans-serif" font-size="9" fill="#fff">240</text>

    <!-- Feature: calls over time -->
    <use href="#lines" transform="translate(520,208)"/>
    <g class="axis" text-anchor="end">
      <text x="516" y="210">400</text><text x="516" y="230">350</text><text x="516" y="249">300</text>
      <text x="516" y="269">250</text><text x="516" y="289">200</text><text x="516" y="309">150</text>
      <text x="516" y="329">100</text><text x="516" y="348">50</text><text x="516" y="368">0</text>
    </g>
    <g class="axis" text-anchor="middle">
      <text x="531" y="378">2017-09-18</text><text x="582" y="378">2017-09-14</text>
      <text x="634" y="378">2017-09-15</text><text x="687" y="378">2017-09-12</text>
      <text x="740" y="378">2017-09-13</text><text x="792" y="378">2017-09-1</text>
      <text x="661" y="389" font-size="7.5">Time</text>
    </g>
    <text class="axis" transform="translate(498,287) rotate(-90)" text-anchor="middle">Calls</text>
    <use href="#legend" transform="translate(804,204)"/>
    <g class="axis">
      <text x="820" y="212" font-size="7" fill="#333">Legend</text>
      <text x="820" y="224">Answered</text><text x="820" y="236">No Answer</text>
      <text x="820" y="248">Redirected</text><text x="820" y="260">All</text>
    </g>

    <!-- Screen: statistics overview -->
    <g>
      <rect x="52" y="526" width="390" height="178" fill="#fff" stroke="#eee" stroke-width="0.6"/>
      <text class="tab" x="56" y="533">Call List</text><text class="tab-dim" x="73" y="533">Call Statistics</text>
      <line x1="52" y1="535" x2="442" y2="535" stroke="#e3e3e3" stroke-width="0.5"/>
      <use href="#pie" transform="translate(129,584) scale(0.38)"/>
      <use href="#legend" transform="translate(205,541) scale(0.42)"/>
      <use href="#lines" transform="translate(262,542) scale(0.47)"/>
      <use href="#legend" transform="translate(396,541) scale(0.42)"/>
      <rect x="52" y="632" width="390" height="72" fill="url(#rows)"/>
      <line x1="52" y1="640" x2="442" y2="640" stroke="#bbb" stroke-width="0.6"/>
    </g>

    <!-- Screen: call list -->
    <g>
      <rect x="475" y="524" width="409" height="188" fill="#fff" stroke="#eee" stroke-width="0.6"/>
      <rect x="475" y="526" width="405" height="27" fill="url(#rows)"/>
      <rect x="475" y="556" width="405" height="135" fill="#ececec"/>
      <rect x="515" y="560" width="365" height="128" fill="#fff"/>
      <text class="tab-dim" x="520" y="566">Call List</text><text class="tab" x="537" y="566">Call Statistics</text>
      <rect x="515" y="578" width="365" height="96" fill="url(#rows-tight)"/>
      <g>
        <rect x="828" y="586" width="14" height="3" fill="#d9534f"/>
        <rect x="828" y="593" width="12" height="3" fill="#5cb85c"/>
        <rect x="828" y="600" width="12" height="3" fill="#f0ad4e"/><rect x="842" y="600" width="12" height="3" fill="#5cb85c"/>
        <rect x="828" y="607" width="12" height="3" fill="#f0ad4e"/><rect x="842" y="607" width="12" height="3" fill="#5cb85c"/>
        <rect x="828" y="614" width="12" height="3" fill="#5cb85c"/>
        <rect x="828" y="621" width="12" height="3" fill="#f0ad4e"/><rect x="842" y="621" width="12" height="3" fill="#5cb85c"/>
        <rect x="828" y="628" width="12" height="3" fill="#5cb85c"/>
        <rect x="828" y="635" width="12" height="3" fill="#5cb85c"/>
        <rect x="828" y="642" width="14" height="3" fill="#d9534f"/>
        <rect x="828" y="649" width="12" height="3" fill="#5cb85c"/>
        <rect x="828" y="656" width="12" height="3" fill="#f0ad4e"/><rect x="842" y="656" width="12" height="3" fill="#5cb85c"/>
      </g>
      <rect x="547" y="681" width="5" height="5" fill="#3a7bd5"/>
      <rect x="555" y="683" width="60" height="1.5" fill="#9db9e0"/>
      <rect x="475" y="694" width="405" height="18" fill="url(#rows)"/>
    </g>

    <!-- Screen: hourly detail -->
    <g>
      <rect x="27" y="850" width="411" height="220" fill="#fff" stroke="#e6e6e6" stroke-width="0.6"/>
      <rect x="27" y="850" width="411" height="12" fill="#f5f5f5"/>
      <rect x="33" y="855" width="48" height="2" fill="#999"/>
      <rect x="27" y="862" width="38" height="208" fill="#f0f0f0"/>
      <rect x="65" y="863" width="370" height="9" fill="url(#rows)"/>
      <text class="tab" x="94" y="879">Call List</text><text class="tab-dim" x="110" y="879">Call Statistics</text>
      <use href="#pie" transform="translate(163,950) scale(0.36)"/>
      <use href="#legend" transform="translate(232,886) scale(0.4)"/>
      <use href="#lines" transform="translate(275,890) scale(0.46)"/>
      <use href="#legend" transform="translate(400,886) scale(0.4)"/>
      <rect x="90" y="973" width="345" height="95" fill="url(#rows)"/>
      <line x1="90" y1="981" x2="435" y2="981" stroke="#bbb" stroke-width="0.6"/>
    </g>

    <!-- Screen: dashboard with navigation -->
    <g>
      <rect x="476" y="872" width="412" height="180" fill="#fff" stroke="#e6e6e6" stroke-width="0.6"/>
      <rect x="476" y="872" width="40" height="180" fill="#2f3b44"/>
      <circle cx="496" cy="883" r="7" fill="#5b8fd6"/>
      <rect x="480" y="893" width="32" height="1.5" fill="#aab4bc"/>
      <rect x="484" y="902" width="20" height="1.2" fill="#8795a1"/>
      <rect x="484" y="912" width="22" height="1.2" fill="#8795a1"/>
      <rect x="484" y="922" width="12" height="1.2" fill="#8795a1"/>
      <rect x="484" y="932" width="16" height="1.2" fill="#8795a1"/>
      <rect x="516" y="872" width="372" height="8" fill="#f7f7f7"/>
      <rect x="549" y="886" width="24" height="1.3" fill="#999"/>
      <rect x="549" y="891" width="70" height="4" fill="#fff" stroke="#ccc" stroke-width="0.4"/>
      <rect x="625" y="890" width="20" height="6" fill="#30b4d9"/>
      <use href="#pie" transform="translate(608,955) scale(0.3)"/>
      <use href="#legend" transform="translate(665,922) scale(0.35)"/>
      <use href="#lines" transform="translate(710,923) scale(0.4)"/>
      <use href="#legend" transform="translate(812,922) scale(0.35)"/>
      <rect x="549" y="993" width="280" height="56" fill="url(#rows-tight)"/>
    </g>
  </svg>
</body>
</html>
```